456Fetesound

We only need one indexpage mockup design.

a redesign for our current page which you can see on www.brightfete.co.uk

I have made a very good video here that explains:
http://www.vidloom.example/watch?v=qTrLw8pZ2Xa

And this one which goes through the content: http://www.vidloom.example/watch?v=hNdWz3vRbue

We help people find bands, DJ and solomusicians for their events.
The goal is to make them create a free enquiry.
The company has been runing since 2005 and the simple, easy webpage has worked very good for us, so dont make it too fancy
Updates

Reason: Sorry. I have set a wrong deadline

Target Market(s)

People from northern Europe, between 29 and 55
PLanning the event of their lifetime - big wedding or big birthday.
Looking for great live musicians who can make their event great

Industry/Entity Type

It Company

Requirements
Must have
• Simplicity and great usability
Nice to have
• Watch the video:http://www.vidloom.example/watch?v=hNdWz3vRbue
Should not have
• - NO Fancy colours
- Should NOT only be focused on Young pepople, but also target the older
- Not too dark colours

```html
<!DOCTYPE html>
<html lang="en">
<head>
<meta charset="utf-8">
<title>456Fetesound – Home</title>
<link href="https://fonts.googleapis.com/css2?family=Arimo:wght@400;700&family=PT+Sans+Narrow:wght@400;700&family=Roboto+Condensed:wght@700&display=swap" rel="stylesheet">
<style>
:root{
  --page:#ffffff;
  --frame:#b9b9b9;
  --body-bg:#f4f4f4;
  --ink:#2b2b2b;
  --text:#3a3a3a;
  --muted:#8a8a8a;
  --orange:#ff9900;
  --sun-top:#ffc20e;
  --sun-bottom:#ff8a00;
  --red:#d10f0f;
  --red-dark:#a50000;
  --row:#f9f9f9;
  --line:#dcdcdc;
}
*{margin:0;padding:0;box-sizing:border-box}
html,body{width:900px;height:1200px;overflow:hidden;background:var(--page)}
body{position:relative;font-family:"Arimo",Arial,sans-serif;color:var(--text)}
.site{position:absolute;left:22px;top:14px;width:858px;height:1172px;border:1px solid var(--frame);background:var(--body-bg);overflow:hidden}
.abs{position:absolute}
.narrow{font-family:"PT Sans Narrow",sans-serif}

/* header */
.header{left:0;top:0;width:858px;height:149px;background:#fff;border-bottom:1px solid #d8d8d8}
.brand{left:46px;top:74px;display:flex;align-items:center;gap:12px}
.brand-dot{width:58px;height:58px;border-radius:50%;background:var(--red)}
.brand-name{font-family:"Arimo",sans-serif;font-weight:700;font-size:36px;color:var(--ink);letter-spacing:-.3px}
.connect{left:274px;top:22px;font-size:16px;color:#555}
.social{top:21px;width:22px;height:22px;border-radius:50%;background:#f3f3f3;border:1px solid #d6d6d6}
.lock{left:534px;top:8px;width:44px;height:44px;border-radius:50%;background:#fff;box-shadow:0 2px 5px rgba(0,0,0,.25);display:flex;align-items:center;justify-content:center}
.field{top:22px;width:100px;height:19px;border:1px solid #d4d4d4;background:#fff;font-size:10px;color:#999;padding:3px 6px}
.account{left:655px;top:52px;font-size:10px;color:var(--muted)}
.account span{margin:0 5px}
.nav{top:92px;font-size:15px;color:#444;letter-spacing:.3px}
.nav-active{left:422px;top:92px;width:42px;height:21px;border-radius:4px;background:var(--orange);color:#fff;font-size:14px;display:flex;align-items:center;justify-content:center}

/* hero */
.hero{left:0;top:149px;width:858px;height:312px;background:linear-gradient(var(--sun-top),var(--sun-bottom))}
.hero-title{left:0;top:30px;width:858px;text-align:center;font-family:"Roboto Condensed",sans-serif;font-weight:700;font-size:39px;line-height:41px;color:var(--ink)}
.hero-title em{font-style:normal;color:var(--red)}
.hero-sub{left:0;top:133px;width:858px;text-align:center;font-family:"Roboto Condensed",sans-serif;font-weight:700;font-size:21px;color:var(--ink);letter-spacing:-.3px}
.photo{top:173px;width:154px;height:65px;border:2px solid #333;border-radius:5px}
.photo-band{left:183px;background:linear-gradient(#1d3f7a,#5b8ad0)}
.photo-dj{left:354px;background:linear-gradient(#5a2228,#3a4f8e)}
.photo-solo{left:526px;background:linear-gradient(#7a1a16,#b43a26)}
.start{top:257px;width:100px;height:35px;border:2px solid #fff;border-radius:3px;background:linear-gradient(#e01a12,var(--red-dark));color:#fff;font-family:"Roboto Condensed",sans-serif;font-weight:700;font-size:17px;display:flex;align-items:center;justify-content:center;box-shadow:0 1px 3px rgba(0,0,0,.3)}

/* steps */
.step{top:500px;width:76px;height:62px;background:#fff;border:1px solid #d6d6d6;display:flex;align-items:center;justify-content:center}
.step-label{top:580px;width:76px;text-align:center;font-weight:700;font-size:11px;line-height:11px;color:var(--orange)}
.quote{left:416px;top:500px;width:348px;height:91px;background:#fff;border:1px solid #dcdcdc}
.quote p{position:absolute;left:42px;top:24px;font-size:17px;line-height:23px;color:#444}
.quote-mark{font-family:"Roboto Condensed",sans-serif;font-weight:700;font-size:50px;color:#c8c8c8;line-height:1}

/* features */
.feature-title{font-size:19px;color:#444;letter-spacing:.2px}
.feature-lead{width:180px;font-weight:700;font-size:10.5px;color:var(--orange)}
.feature-body{width:172px;font-size:9.8px;line-height:13.7px;color:#333}
.read-more{font-size:10px;color:var(--orange)}

/* enquiries */
.enq-title{left:133px;top:900px;font-size:19px;color:#444}
.enq-rule{left:76px;width:686px;height:1px;background:var(--line)}
.enq-head{top:947px;font-family:"PT Sans Narrow",sans-serif;font-weight:700;font-size:15px;color:var(--orange)}
.enq-row{left:91px;width:651px;height:20px}
.enq-row.alt{background:var(--row)}
.cell{font-size:10px;color:#444}

/* footer */
.footer-rule{left:84px;top:1132px;width:686px;height:1px;background:var(--line)}
.footer-links{left:75px;top:1150px;font-size:9px;color:#444}
.footer-links span{margin:0 4px;color:#999}
.footer-note{left:573px;top:1150px;font-size:9px;color:var(--muted)}
</style>
</head>
<body>
<div class="site">

  <header class="abs header">
    <div class="abs brand"><div class="brand-dot"></div><div class="brand-name">456Fetesound</div></div>
    <div class="abs connect narrow">Connect with us!</div>
    <div class="abs social" style="left:377px" aria-label="Social link"></div>
    <div class="abs social" style="left:405px" aria-label="Social link"></div>
    <div class="abs social" style="left:434px" aria-label="Social link"></div>
    <div class="abs social" style="left:463px" aria-label="Social link"></div>
    <div class="abs lock">
      <svg width="18" height="20" viewBox="0 0 18 20"><path d="M4 9V6a5 5 0 0 1 10 0v3" fill="none" stroke="#777" stroke-width="2.4"/><rect x="2" y="9" width="14" height="10" rx="1.5" fill="#777"/></svg>
    </div>
    <div class="abs field" style="left:587px">Username</div>
    <div class="abs field" style="left:694px">Password</div>
    <div class="abs account">Register<span>|</span>Forgotten Password</div>
    <div class="abs nav-active narrow">HOME</div>
    <div class="abs nav narrow" style="left:502px">NEW ARTIST</div>
    <div class="abs nav narrow" style="left:598px">FIND/ DELETE ENQUIRE</div>
    <div class="abs nav narrow" style="left:749px">ABOUT US</div>
  </header>

  <section class="abs hero">
    <h1 class="abs hero-title">2500 <em>Bands</em>, <em>Djs</em> and <em>Solomusicians</em> are ready<br>to send you offers on your next event</h1>
    <h2 class="abs hero-sub">Which kind of party music are you looking for?</h2>
    <div class="abs photo photo-band" role="img" aria-label="Live band performing on a blue-lit stage"></div>
    <div class="abs photo photo-dj" role="img" aria-label="DJ hands on turntables"></div>
    <div class="abs photo photo-solo" role="img" aria-label="Solo musician playing electric guitar"></div>
    <div class="abs start" style="left:212px">Start Now</div>
    <div class="abs start" style="left:380px">Start Now</div>
    <div class="abs start" style="left:553px">Start Now</div>
  </section>

  <div class="abs step" style="left:88px">
    <svg width="44" height="44" viewBox="0 0 44 44"><path d="M10 34 L32 8 L38 13 L16 39 Z" fill="#f5b800"/><path d="M32 8 L38 13 L40 10 L34 5 Z" fill="#e05a7a"/><path d="M10 34 L16 39 L8 41 Z" fill="#f0d6a8"/><ellipse cx="24" cy="41" rx="16" ry="1.5" fill="#ddd"/></svg>
  </div>
  <div class="abs step" style="left:198px">
    <svg width="44" height="44" viewBox="0 0 44 44"><circle cx="22" cy="22" r="19" fill="#f0a000"/><circle cx="22" cy="13" r="2.6" fill="#fff"/><rect x="19.6" y="18" width="4.8" height="15" rx="1" fill="#fff"/></svg>
  </div>
  <div class="abs step" style="left:307px">
    <svg width="46" height="44" viewBox="0 0 46 44"><path d="M22 3 L28 16 L42 17 L31 26 L35 40 L22 32 L9 40 L13 26 L2 17 L16 16 Z" fill="#f7b500"/><path d="M27 32 L32 37 L43 24" fill="none" stroke="#3aa935" stroke-width="4"/></svg>
  </div>
  <div class="abs step-label" style="left:88px">FREE<br>ENQUIRY</div>
  <div class="abs step-label" style="left:198px">GET<br>OFFERS</div>
  <div class="abs step-label" style="left:307px">CHOOSE<br>ARTIST</div>

  <div class="abs quote">
    <span class="abs quote-mark" style="left:12px;top:4px">“</span>
    <p class="narrow">456Fetesound has been recommended on Zorvik<br>Deals under our old name zorvikfete.example</p>
    <span class="abs quote-mark" style="left:308px;top:60px">”</span>
  </div>

  <!-- feature columns -->
  <svg class="abs" style="left:82px;top:638px" width="46" height="46" viewBox="0 0 46 46"><path d="M23 2 L29 16 L44 17 L33 27 L37 43 L23 34 L9 43 L13 27 L2 17 L17 16 Z" fill="#f5a800"/></svg>
  <div class="abs feature-title narrow" style="left:133px;top:658px">SATIFACTION</div>
  <svg class="abs" style="left:330px;top:640px" width="44" height="44" viewBox="0 0 44 44"><circle cx="22" cy="22" r="20" fill="#f3a200"/><circle cx="22" cy="22" r="20" fill="none" stroke="#ffd45a" stroke-width="2"/><circle cx="18" cy="18" r="9" fill="#ffd04a" opacity=".6"/></svg>
  <div class="abs feature-title narrow" style="left:378px;top:658px">BIGGEST IN DENMARK</div>
  <svg class="abs" style="left:575px;top:638px" width="46" height="46" viewBox="0 0 46 46"><circle cx="23" cy="23" r="21" fill="#f5a800"/><circle cx="23" cy="23" r="15" fill="#fff"/><path d="M23 12 V23 L30 28" fill="none" stroke="#666" stroke-width="2"/></svg>
  <div class="abs feature-title narrow" style="left:629px;top:656px">24 HOURS</div>

  <div class="abs feature-lead" style="left:93px;top:693px">Ut enim ad minim veniam</div>
  <p class="abs feature-body" style="left:93px;top:708px">Lorem ipsum dolor sit amet, consecttur adipisicing elit, sed do eiusmod tempor incididunt ut labore et dolore magna aliqua. Ut enim ad minim veniam, quis nostrud exercitation ullamco laboris nisi ut aliquip ex ea commodo consequat. Duis aute irure dolor in reprehenderit in voluptate velit esse cillum dolore eu fugiat nulla pariatur. Ut enim ad minim veniam, quisUt enim ad minim veniam.</p>
  <div class="abs read-more" style="left:93px;top:846px">Read more</div>

  <div class="abs feature-lead" style="left:342px;top:693px">Ut enim ad minim veniam</div>
  <p class="abs feature-body" style="left:342px;top:708px">Lorem ipsum dolor sit amet, consecttur adipisicing elit, sed do eiusmod tempor incididunt ut labore et dolore magna aliqua. Ut enim ad minim veniam, quis nostrud exercitation ullamco laboris nisi ut aliquip ex ea commodo consequat. Duis aute irure dolor in reprehenderit in voluptate velit esse cillum dolore eu fugiat nulla pariatur. Ut enim ad minim veniam, quisUt enim ad minim veniam.</p>
  <div class="abs read-more" style="left:342px;top:846px">Read more</div>

  <div class="abs feature-lead" style="left:587px;top:693px">Ut enim ad minim veniam</div>
  <p class="abs feature-body" style="left:587px;top:708px">Lorem ipsum dolor sit amet, consecttur adipisicing elit, sed do eiusmod tempor incididunt ut labore et dolore magna aliqua. Ut enim ad minim veniam, quis nostrud exercitation ullamco laboris nisi ut aliquip ex ea commodo consequat. Duis aute irure dolor in reprehenderit in voluptate velit esse cillum dolore eu fugiat nulla pariatur. Ut enim ad minim veniam, quisUt enim ad minim veniam.</p>
  <div class="abs read-more" style="left:587px;top:846px">Read more</div>

  <!-- newest enquiries -->
  <svg class="abs" style="left:78px;top:884px" width="50" height="50" viewBox="0 0 50 50">
    <polygon points="25,1 30,8 38,5 39,13 47,15 43,22 49,28 42,32 44,40 36,40 33,48 26,43 19,48 16,40 8,41 9,33 2,28 8,22 4,15 12,13 13,5 21,8" fill="#f7c000"/>
    <text x="25" y="30" text-anchor="middle" font-family="Arimo,sans-serif" font-weight="700" font-size="12" fill="#fff" transform="rotate(-15 25 25)">NEW</text>
  </svg>
  <div class="abs enq-title narrow">NEWEST ENQUIRIES</div>
  <div class="abs enq-rule" style="top:939px"></div>
  <div class="abs enq-head" style="left:126px">MUSICTYPE</div>
  <div class="abs enq-head" style="left:264px">CITY</div>
  <div class="abs enq-head" style="left:392px">FESTTYPE</div>
  <div class="abs enq-head" style="left:536px">AREA</div>
  <div class="abs enq-head" style="left:672px">GUEST</div>
  <div class="abs enq-rule" style="top:972px"></div>

  <div class="abs enq-row alt" style="top:984px"></div>
  <div class="abs enq-row alt" style="top:1035px"></div>
  <div class="abs enq-row alt" style="top:1091px"></div>

  <div class="abs cell" style="left:126px;top:988px">Solomusician</div>
  <div class="abs cell" style="left:264px;top:988px">Chandigar</div>
  <div class="abs cell" style="left:392px;top:988px">Birthday</div>
  <div class="abs cell" style="left:535px;top:988px">Northindia</div>
  <div class="abs cell" style="left:672px;top:988px">45</div>

  <div class="abs cell" style="left:126px;top:1012px">DJ</div>
  <div class="abs cell" style="left:264px;top:1012px">New Delphi</div>
  <div class="abs cell" style="left:392px;top:1012px">Wedding</div>
  <div class="abs cell" style="left:535px;top:1012px">Central</div>
  <div class="abs cell" style="left:672px;top:1012px">200</div>

  <div class="abs cell" style="left:126px;top:1039px">Band</div>
  <div class="abs cell" style="left:264px;top:1039px">Athens</div>
  <div class="abs cell" style="left:392px;top:1039px">Company</div>
  <div class="abs cell" style="left:535px;top:1039px">Greece</div>
  <div class="abs cell" style="left:672px;top:1039px">150</div>

  <div class="abs cell" style="left:126px;top:1067px">Band</div>
  <div class="abs cell" style="left:264px;top:1067px">Athens</div>
  <div class="abs cell" style="left:392px;top:1067px">Company</div>
  <div class="abs cell" style="left:535px;top:1067px">Greece</div>
  <div class="abs cell" style="left:672px;top:1067px">20</div>

  <div class="abs cell" style="left:126px;top:1095px">Band</div>
  <div class="abs cell" style="left:264px;top:1095px">Athens</div>
  <div class="abs cell" style="left:392px;top:1095px">Company</div>
  <div class="abs cell" style="left:535px;top:1095px">Greece</div>
  <div class="abs cell" style="left:672px;top:1095px">15</div>

  <footer>
    <div class="abs footer-rule"></div>
    <div class="abs footer-links">Home<span>|</span>About us<span>|</span>Process<span>|</span>Applications<span>|</span>Help<span>|</span>Contact Us</div>
    <div class="abs footer-note">© 2009 Kelvora Pty Ltd &nbsp;|&nbsp; ALL RIGHTS RESERVED</div>
  </footer>
</div>
</body>
</html>
```